Redesign Of Current Landing Page

I need to redesign this landing page https://www.brightoakpromos.biz/?page=landing&landing=23 (Please do not opt in because when you do it will show you the home page. Please clear your cookies before going to this url above to view the 1 page landing page.)

Please use my updated website as a reference for colors and logo.
http://layoutcraftzone.com/dh/bopg/index.html

I would like the call to action to be a button that opens into a lead form...

Button would be "Download Samples"

small business owners

Marketing

1 page

Designer to choose colors to be used in the design.

• must be full responsive on all devices
• must have a legitimate professional apeal to it
• open

```html
<!DOCTYPE html>
<html lang="en">
<head>
<meta charset="utf-8">
<title>Bright Oak Promos Group – Landing</title>
<link href="https://fonts.googleapis.com/css2?family=Raleway:ital,wght@0,400;0,500;0,600;0,700;0,800;1,400&display=swap" rel="stylesheet">
<style>
  :root{
    --blue:#0a6fc2;
    --ink:#222;
    --text:#333;
    --band:#50555f;
    --footer:#1f1f1f;
    --white:#fff;
    --muted:#bfc2c7;
  }
  *{box-sizing:border-box;margin:0;padding:0}
  html,body{width:821px;height:1200px;overflow:hidden}
  body{font-family:'Raleway',sans-serif;color:var(--text);background:var(--white);position:relative}
  .site-header{height:69px;position:relative}
  .brand{position:absolute;left:52px;top:20px;display:flex;align-items:center;gap:7px}
  .brand-mark{width:26px;height:26px;border-radius:50%;background:var(--blue)}
  .brand-name{font-weight:800;font-size:22px;letter-spacing:1px;color:var(--ink)}
  .cta-download{position:absolute;left:624px;top:22px;width:146px;height:31px;border-radius:16px;background:var(--blue);color:var(--white);font-size:9.5px;font-weight:700;display:flex;align-items:center;justify-content:center;letter-spacing:.3px;text-decoration:none}
  .hero{position:absolute;top:69px;left:0;width:821px;height:361px;background:linear-gradient(120deg,#8a7d72 0%,#b9b2a8 30%,#d6d3cd 55%,#6f6258 80%,#4f5866 100%)}
  .hero-caption{position:absolute;left:213px;top:135px;width:394px;height:92px;background:rgba(40,40,40,.72);text-align:center;padding-top:10px}
  .hero-title{color:var(--blue);font-size:25px;font-weight:800;letter-spacing:.2px}
  .hero-sub{color:var(--white);font-size:15.5px;font-weight:700;line-height:20px;margin-top:2px}
  .hero-dots{position:absolute;left:50px;top:315px;display:flex;gap:7px}
  .hero-dots span{width:9px;height:9px;border-radius:50%;background:var(--white)}
  .hero-dots span.active{background:var(--blue)}
  .intro{position:absolute;top:460px;left:0;width:821px}
  .intro-col{position:absolute;width:350px}
  .intro-col h2{color:var(--blue);font-size:16px;font-weight:700;letter-spacing:.3px;margin-bottom:12px}
  .intro-col p{font-size:9.6px;line-height:16.5px;margin-bottom:2px}
  .btn-more{position:absolute;top:147px;width:103px;height:29px;border-radius:15px;background:#151515;color:var(--white);font-size:9.5px;font-weight:700;display:flex;align-items:center;justify-content:center}
  .benefits{position:absolute;top:675px;left:0;width:821px;height:241px;background:var(--band);color:var(--white)}
  .benefits h2{text-align:center;font-size:16px;font-weight:600;margin-top:34px;letter-spacing:.2px}
  .benefit{position:absolute;display:flex;align-items:center;gap:10px;font-size:10.5px;line-height:14.5px;color:#e8e9eb}
  .benefit-icon{width:52px;height:52px;border:2px solid var(--white);border-radius:50%;display:flex;align-items:center;justify-content:center;flex:none}
  .testimonials{position:absolute;top:945px;left:0;width:821px;text-align:center}
  .testimonials h2{color:var(--blue);font-size:16px;font-weight:700}
  .quote{font-style:italic;font-size:9.5px;line-height:16.5px;width:640px;margin:8px auto 0}
  .author{color:var(--blue);font-size:9.5px;margin-top:8px}
  .place{font-style:italic;font-size:9.5px;margin-top:3px}
  .site-footer{position:absolute;top:1113px;left:0;width:821px;height:87px;background:var(--footer)}
  .copyright{position:absolute;left:53px;top:32px;color:var(--muted);font-size:8.8px;line-height:13px}
  .social{position:absolute;left:624px;top:38px;display:flex;gap:13px}
  .social span{width:13px;height:13px;border-radius:2px;background:#9a9a9a}
</style>
</head>
<body>
<header class="site-header">
  <div class="brand"><span class="brand-mark"></span><span class="brand-name">BOPG</span></div>
  <a class="cta-download" href="#">DOWNLOAD SAMPLES</a>
</header>

<section class="hero" role="img" aria-label="Photo of a team meeting around an office table with a laptop showing a chart">
  <div class="hero-caption">
    <div class="hero-title">ATTRACT MORE CUSTOMERS</div>
    <div class="hero-sub">Who spend more money with your business<br>more often!</div>
  </div>
  <div class="hero-dots"><span class="active"></span><span></span><span></span><span></span></div>
</section>

<section class="intro">
  <div class="intro-col" style="left:51px">
    <h2>IMAGINE</h2>
    <p>Being able to create exciting give away promotions that will boost your sales without ever having to worry about cost.</p>
    <p>Bright Oak Promos Group, Inc. provides high-perceived value promotional incentives to businesses that want to advertise an exciting Give Away that will instantly attract more customers from your existing advertising efforts.</p>
    <div class="btn-more">READ MORE</div>
  </div>
  <div class="intro-col" style="left:420px">
    <h2>HOW CAN WE DO IT?</h2>
    <p>We help fill empty rooms for thousands of hotels and resorts in hundreds of destinations around the world as well as the major cruise lines. Hotels and resorts are rarely full so when we place someone in their empty rooms, they end up making it up when travelers spend money on room service, spa services, eat at their in-house restaurants, casino and take advantage of other amenities that drive revenue.</p>
    <div class="btn-more">READ MORE</div>
  </div>
</section>

<section class="benefits">
  <h2>WHY OFFER INCENTIVES TO CUSTOMERS?</h2>
  <div class="benefit" style="left:51px;top:74px">
    <span class="benefit-icon"><svg width="22" height="18" viewBox="0 0 22 18" fill="none" stroke="#fff" stroke-width="2"><path d="M1 1v16h20"/><path d="M4 13l5-5 4 3 6-7"/></svg></span>
    <span>Increase Responses From<br>Your Existing Ads</span>
  </div>
  <div class="benefit" style="left:298px;top:74px">
    <span class="benefit-icon"><svg width="20" height="20" viewBox="0 0 20 20"><path d="M13 1a5 5 0 0 0-4.6 6.8L1.5 14.7a2 2 0 0 0 2.8 2.8l6.9-6.9A5 5 0 0 0 18 5.5l-3 3-3-1-1-3 3-3z" fill="#fff"/></svg></span>
    <span>#1 Sales Closing Tool -<br>Gift w/ Purchase</span>
  </div>
  <div class="benefit" style="left:543px;top:74px">
    <span class="benefit-icon"><svg width="20" height="20" viewBox="0 0 24 24"><path d="M12 1.5l3.2 6.6 7.3 1-5.3 5.1 1.3 7.3L12 18l-6.5 3.5 1.3-7.3L1.5 9.1l7.3-1z" fill="#fff"/></svg></span>
    <span>Build Brand Awareness<br>and Trust</span>
  </div>
  <div class="benefit" style="left:51px;top:149px">
    <span class="benefit-icon"><svg width="22" height="18" viewBox="0 0 22 18" fill="#fff"><circle cx="11" cy="5" r="3.5"/><circle cx="4.5" cy="6.5" r="2.5"/><circle cx="17.5" cy="6.5" r="2.5"/><path d="M5 17c0-4 2.7-6.5 6-6.5s6 2.5 6 6.5z"/><path d="M0 15c0-3 1.8-5 4.5-5 1 0 1.6.3 1.6.3C4.8 11.6 4.2 13 4 15z"/><path d="M22 15c0-3-1.8-5-4.5-5-1 0-1.6.3-1.6.3 1.3 1.3 1.9 2.7 2.1 4.7z"/></svg></span>
    <span>Insure The Sale Over Your<br>Competition</span>
  </div>
  <div class="benefit" style="left:298px;top:149px">
    <span class="benefit-icon"><svg width="20" height="16" viewBox="0 0 20 16" fill="#fff"><path d="M1 4h13V1l5 4.5-5 4.5V7H1z"/><path d="M19 12H6v3l-5-4.5L6 6v3h13z" transform="translate(0 1)"/></svg></span>
    <span>Boost Repeat and Referral<br>Business</span>
  </div>
  <div class="benefit" style="left:543px;top:149px">
    <span class="benefit-icon"><svg width="24" height="16" viewBox="0 0 24 16" fill="none" stroke="#fff" stroke-width="2"><rect x="1" y="1" width="22" height="14"/><circle cx="12" cy="8" r="3.5"/><path d="M4 4v8M20 4v8"/></svg></span>
    <span>Improve Retention<br>Rates</span>
  </div>
</section>

<section class="testimonials">
  <h2>TESTIMONIALS</h2>
  <p class="quote">“ I began using your incentives two years ago to boost lead generation efforts. I have experienced a 63% increase in lead captures. And, even more importantly, my sales have increased as well. The ability to offer unlimited certificates and not having to pay for each certificate I give away is perhaps the best feature of the program, but having the flexibility to email or print certificates for my customers is also wonderful. I even use your html banners to automate my promotions right on my website!...”</p>
  <p class="author">Dana R.</p>
  <p class="place">Fairbrook, OH</p>
</section>

<footer class="site-footer">
  <p class="copyright">Copyright © 2005-2017 Bright Oak Promos Group, Inc.<br>All Rights Reserved</p>
  <div class="social" aria-label="Social links"><span></span><span></span><span></span><span></span><span></span><span></span></div>
</footer>
</body>
</html>
```